Personal Business Card

Looking for a clean and modern personal business card. Basically I need something catchy to give to potential clients and people I meet. I do a lot of freelancing (from DJ'ing to wedding videography, but its mostly on the event side of things) so it's more-so about selling myself rather than identifying with a company. I'm starting to meet more people that I want to work with after meeting them so I'm revamping my business cards.

I'm looking for a clean and modern design- I know that's really vague but I'm fine with anything ranging from a symbol to just a fancy version of my name.

Details I need on the front:
Dennis Kowal
dennis@denniskowal-mail.net
(555) 807-2291

On the back I'd like to have something simple like "Nice to have met you today" or "Great meeting you".

UPDATE 9/27 Noon: My apologies for not putting it up before- I'm definitely looking for full color. Doesn't have to be a rainbow but I am looking for the least amount of blank white as possible.

UPDATE 10/1: Really impressed with what I've been getting so far and I'm working on giving everyone feedback- if your design is still up then you're still in the run. Looking for something more unique and modern so please do not post something that looks like a template from Cardloom!

Target Market(s)

Mainly to give to people aged 18-35. Most of my encounters will be casual so the card should have a "young" feeling to it. I rarely do anything in the corporate world so it doesn't have to be boring. It should give the impression that I'm the one they should go to if they need what I do (again it changes every weekend so I'll probably say the "what I do" part.

Industry/Entity Type

Wedding

Requirements
Must have
• Basically the contact information listed above
Nice to have
• I really like the colors Blue, Silver, and Purple. They don't have to necessarily all be there though. I do like the look of polished metal if that makes sense.
Should not have
• A template that resembles card-loom. I'm in a point in my life where I'm working a lot of different markets/areas so the card does not need to have an address or address placeholder.

```html
<!DOCTYPE html>
<html lang="en">
<head>
<meta charset="utf-8">
<title>Dennis Kowal – Business Card</title>
<link href="https://fonts.googleapis.com/css2?family=Russo+One&family=Libre+Baskerville:wght@400;700&display=swap" rel="stylesheet">
<style>
  :root {
    --page-bg: #e6e7e9;
    --plate-dark: #0c0f3a;
    --plate-mid: #1f2a8c;
    --plate-light: #3d4fc4;
    --steel-light: #f2f4f4;
    --steel-mid: #a9b0b2;
    --steel-dark: #4e5558;
    --ink: #111213;
    --chrome-top: #9fd2ff;
    --chrome-mid: #1b6fd6;
    --chrome-deep: #0a1f6e;
    --card-shadow: rgba(0,0,0,0.45);
  }
  * { margin: 0; padding: 0; box-sizing: border-box; }
  html, body {
    width: 1200px; height: 1000px; overflow: hidden;
    background: var(--page-bg);
  }
  .canvas { position: relative; width: 1200px; height: 1000px; }

  .card {
    position: absolute;
    width: 697px; height: 402px;
    overflow: hidden;
    box-shadow: 3px 4px 5px var(--card-shadow);
  }
  .card--front { left: 98px; top: 76px; }
  .card--back  { left: 406px; top: 522px; }

  .plate-band {
    position: absolute; left: 0; width: 100%;
    background:
      radial-gradient(ellipse at 30% 40%, var(--plate-light) 0%, transparent 45%),
      radial-gradient(ellipse at 75% 60%, var(--plate-light) 0%, transparent 40%),
      linear-gradient(180deg, var(--plate-mid), var(--plate-dark));
  }
  .plate-band--top { top: 0; height: 54px; }
  .plate-band--bottom { bottom: 0; height: 58px; background:
      radial-gradient(ellipse at 40% 50%, var(--plate-mid) 0%, transparent 50%),
      linear-gradient(180deg, var(--plate-dark), #070922); }

  .steel-panel {
    position: absolute; left: 0; top: 54px; width: 100%; height: 290px;
    background:
      radial-gradient(ellipse 45% 60% at 62% 18%, rgba(255,255,255,0.85), transparent 70%),
      linear-gradient(180deg, rgba(0,0,0,0) 55%, rgba(0,0,0,0.55) 100%),
      linear-gradient(90deg, var(--steel-dark) 0%, var(--steel-mid) 25%, var(--steel-light) 60%, var(--steel-mid) 85%, var(--steel-dark) 100%);
    box-shadow: 0 2px 4px rgba(0,0,0,0.6), 0 -2px 4px rgba(0,0,0,0.5);
  }

  .card-name {
    position: absolute; left: 0; width: 100%; top: 124px;
    text-align: center;
    font-family: "Russo One", sans-serif;
    font-size: 64px; line-height: 1;
    letter-spacing: 2px;
    text-transform: uppercase;
    background: linear-gradient(180deg, var(--chrome-top) 0%, var(--chrome-mid) 45%, var(--chrome-deep) 55%, var(--chrome-mid) 80%, var(--chrome-top) 100%);
    -webkit-background-clip: text; background-clip: text;
    color: transparent;
    filter: drop-shadow(2px 3px 2px rgba(0,0,0,0.7));
  }

  .contact {
    position: absolute; left: 0; width: 100%; top: 224px;
    text-align: center;
    font-family: "Libre Baskerville", serif;
    font-size: 25px; line-height: 33px;
    color: var(--ink);
    text-shadow: 1px 2px 2px rgba(0,0,0,0.35);
  }

  .greeting {
    position: absolute; left: 0; width: 100%; top: 170px;
    text-align: center;
    font-family: "Libre Baskerville", serif;
    font-weight: 700; font-size: 41px; line-height: 1;
    color: var(--ink);
    text-shadow: 2px 3px 3px rgba(0,0,0,0.4);
  }
</style>
</head>
<body>
<main class="canvas">
  <section class="card card--front" aria-label="Card front">
    <div class="plate-band plate-band--top" role="img" aria-label="Blue diamond-plate metal band"></div>
    <div class="steel-panel"></div>
    <div class="plate-band plate-band--bottom" role="img" aria-label="Blue diamond-plate metal band"></div>
    <h1 class="card-name">Dennis Kowal</h1>
    <p class="contact">dennis@denniskowal-mail.net<br>(555) 807-2291</p>
  </section>

  <section class="card card--back" aria-label="Card back">
    <div class="plate-band plate-band--top" role="img" aria-label="Blue diamond-plate metal band"></div>
    <div class="steel-panel"></div>
    <div class="plate-band plate-band--bottom" role="img" aria-label="Blue diamond-plate metal band"></div>
    <p class="greeting">“Great Meeting You”</p>
  </section>
</main>
</body>
</html>
```